Bright Meadow LLC business card

I help with the Marketing and Sales of various Natural, Organic, Eco Friendly and Healthy Main Stream products to Retail Corporate accounts as well as Independents and Distributors.I also highlight Private label items to these same Retail Corporate accounts.Cherish the Moments, Enjoy Life!

Speciality & Health Sales and Marketing

Target Market(s)

Men and Women

Industry/Entity Type

Business

Contact Information for Business Card

Bright Meadow, LLC
Janet Lou Brindall
418 West Fern Lane
Ste 3-274
Phoenix, AZ 85047
602-555-0173
jbrindall@veltramail.net

Requirements
Must have
• Nice, femine font
Something in the background or on a side with a softness
Nice to have
• Cherish the Moments, Enjoy Life
Should not have
• Hardness

```html
<!DOCTYPE html>
<html lang="en">
<head>
<meta charset="utf-8">
<title>Bright Meadow LLC — Business Card</title>
<link rel="stylesheet" href="https://fonts.googleapis.com/css2?family=Lobster&family=Quicksand:wght@500&display=swap">
<style>
  :root {
    --backdrop: #262626;
    --card-paper: #ececea;
    --leaf-lime: #9dc43b;
    --leaf-olive: #8ca75f;
    --ink: #151515;
  }
  * { margin: 0; padding: 0; box-sizing: border-box; }
  html, body {
    width: 1200px;
    height: 1000px;
    overflow: hidden;
    background: var(--backdrop);
  }
  .canvas {
    width: 1200px;
    height: 1000px;
    display: flex;
    align-items: center;
    justify-content: center;
  }
  .business-card {
    position: relative;
    width: 700px;
    height: 400px;
    background: var(--card-paper);
    overflow: hidden;
  }
  .leaf-artwork {
    position: absolute;
    top: 0;
    left: 0;
    width: 330px;
    height: 400px;
    border-top-right-radius: 100% 100%;
    background: linear-gradient(100deg, var(--leaf-lime) 0%, var(--leaf-lime) 55%, var(--leaf-olive) 100%);
  }
  .company-name {
    position: absolute;
    top: 48px;
    right: 52px;
    font-family: "Lobster", cursive;
    font-weight: 400;
    font-size: 44px;
    color: var(--ink);
    letter-spacing: 0.5px;
  }
  .contact-block {
    position: absolute;
    right: 52px;
    bottom: 56px;
    font-family: "Quicksand", sans-serif;
    font-style: normal;
    font-weight: 500;
    font-size: 17px;
    line-height: 1.45;
    color: var(--ink);
    text-align: right;
    letter-spacing: 0.6px;
  }
  .contact-line { display: block; }
</style>
</head>
<body>
  <main class="canvas">
    <article class="business-card">
      <div class="leaf-artwork" role="img" aria-label="Large soft green leaf illustration in lime and olive tones"></div>
      <h1 class="company-name">Bright Meadow</h1>
      <address class="contact-block">
        <span class="contact-line">LLC Janet Lou Brindall 418</span>
        <span class="contact-line">West Fern Lane Ste 3-274 Phoenix</span>
        <span class="contact-line">AZ 85047</span>
        <span class="contact-line">602-555-0173</span>
        <span class="contact-line">jbrindall@veltramail.net</span>
      </address>
    </article>
  </main>
</body>
</html>
```